Boutique Shoe Bag Race wear Business Card Design

We are a new luxury shoe bag, jewellery and race wear store stocking local and international designers. Located in the fashion precinct of beautiful Bondi Beach famous in Sydney Australia. Stocking French jewellery and shoes such as Maximilien verdacs plus Australian made. Looking at quality and service and looking after the locals and tourists.
Ideas: White background, Black writing in bold engravers, logo in middle of Bondi and Boutique a gold horseshoe (facing upright so the curve is at the bottom) with a black stiletto inside. French clover silver and black border (not irish clover the French lattice type look)

Larkspur Parlour

I open 8/4 so require business card design ASAP.

Please place gold horseshoe facing upwards with the black stiletto inside.

Bold engravers writing for business name.

I will have my phone number tomorrow to update.

Border in similar/same style as attached picture with black/silver clover French design.

Thank you. Petra                                   

Industry/Entity Type

Fashion

Contact Information for Business Card

Larkspur Parlour
Boutique Owner Petra Halvorsen
41B Tindle Road
Wrenhaven NSW 2041 Australia
0491237406
02 **** *TBA
info@larkspurparlour.com.au
Facebook.com/LarkspurParlour
www.larkspurparlour.com.au

Font styles to use
Other font styles liked:
• Bold Engravers

Requirements
Must have
• Info on one side including business name and logo with black stiletto and gold horse shoe. reverse side with French clover border and Larger name Larkspur Parlour with logo in centre.
Should not have
• irish clover
French script
horseshoe upside down

```html
<!DOCTYPE html>
<html lang="en">
<head>
<meta charset="utf-8">
<title>Larkspur Parlour — Business Card</title>
<link href="https://fonts.googleapis.com/css2?family=Cinzel:wght@500;600&family=Marcellus&display=swap" rel="stylesheet">
<style>
  :root {
    --backdrop: #e9e9e9;
    --card: #ffffff;
    --ink: #111111;
    --text: #2a2a2a;
    --lattice: #8f8f8f;
    --frame: #e6e6e6;
    --gold: #c9a23a;
  }
  * { margin: 0; padding: 0; box-sizing: border-box; }
  html, body { width: 1200px; height: 1000px; overflow: hidden; }
  body { background: var(--backdrop); position: relative; }

  .card { position: absolute; background: var(--card); }

  /* Front */
  .card-front { left: 250px; top: 216px; width: 342px; height: 554px; }
  .lattice-border {
    position: absolute; inset: 0;
    background: linear-gradient(135deg, #9c9c9c, var(--lattice) 50%, #7d7d7d);
  }
  .front-panel {
    position: absolute; left: 26px; top: 24px; width: 299px; height: 505px;
    background: var(--card);
    display: flex; flex-direction: column; align-items: center; justify-content: center;
    padding-top: 16px;
  }
  .brand-word {
    font-family: "Cinzel", serif; font-weight: 600; color: var(--ink);
    font-size: 33px; line-height: 1; letter-spacing: 0.5px;
  }
  .brand-mark { width: 70px; height: 70px; margin: 20px 0 22px; }

  /* Back */
  .card-back { left: 631px; top: 215px; width: 342px; height: 555px; }
  .back-frame {
    position: absolute; left: 15px; top: 25px; width: 313px; height: 505px;
    border: 3px solid var(--frame); border-radius: 3px;
  }
  .info {
    position: absolute; left: 77px;
    font-family: "Marcellus", serif; color: var(--text);
    font-size: 15px; line-height: 18px;
  }
  .address { top: 102px; }
  .back-name {
    position: absolute; left: 0; right: 0; top: 243px; text-align: center;
    font-family: "Marcellus", serif; font-size: 22px; color: var(--ink);
  }
  .role { top: 354px; }
  .person { top: 373px; font-size: 19px; color: var(--ink); line-height: 24px; }
  .contact { top: 414px; line-height: 17.5px; }
</style>
</head>
<body>
  <section class="card card-front">
    <div class="lattice-border" role="img" aria-label="Silver and black French lattice pattern border"></div>
    <div class="front-panel">
      <div class="brand-word">LARKSPUR</div>
      <svg class="brand-mark" viewBox="0 0 70 70" aria-hidden="true">
        <circle cx="35" cy="35" r="31" fill="none" stroke="var(--gold)" stroke-width="3.5"/>
      </svg>
      <div class="brand-word">PARLOUR</div>
    </div>
  </section>

  <section class="card card-back">
    <div class="back-frame"></div>
    <p class="info address">41B Tindle Road<br>Wrenhaven NSW 2041<br>Australia 0491237406</p>
    <p class="back-name">Larkspur Parlour</p>
    <p class="info role">Boutique Owner</p>
    <p class="info person">Petra Halvorsen</p>
    <p class="info contact">02 **** *TBA<br>info@larkspurparlour.com.au<br>Facebook.com/LarkspurParlour<br>www.larkspurparlour.com.au</p>
  </section>
</body>
</html>
```